Design some Business Cards for a tax counter

Hi, I am looking to have a business card designed for my work , audit, tax accounting.

What I am looking for:

* I am looking for a double-sided business card

* Front - a place for me to include my personal information and a label (In spanish):
___________________________________________________________________
Nombre: Lorena Fuentes Araya || Asesorías laborales & Contables.
Email: lorena.fuentes.araya@correoviva.cl
Dirección: Av. Palmeral nº 582 oficina 7, Rengo. (DRESS)
Celular: +569 84125093

*Label (in Spanish ): - Asesorías Tributaria
- Asesorías Laborales
______________________________________________________________________
* Back - a theme or colors, i accept ideas

**I am looking for a design that shows sales growth in some way, is very professional, and eye catching.**

Please accept ideas, be creative.

you can use a logo similar to the attachment

Files: .ai .psd. .jpg .jpeg

```html
<!DOCTYPE html>
<html lang="es">
<head>
<meta charset="utf-8">
<title>Nivela Auditoría &amp; Contabilidad – Tarjetas de presentación</title>
<link href="https://fonts.googleapis.com/css2?family=Arimo:wght@400;700&display=swap" rel="stylesheet">
<style>
  :root {
    --backdrop: #c9c9cb;
    --card: #2c2c2f;
    --brand-blue: #2aa6e0;
    --bar-grey: #6d6d72;
    --text-light: #e6e6e6;
    --text-muted: #a9a9ad;
    --rule: #8a8a8f;
  }
  * { margin: 0; padding: 0; box-sizing: border-box; }
  html, body {
    width: 1200px;
    height: 900px;
    overflow: hidden;
    background: var(--backdrop);
    font-family: "Arimo", Arial, sans-serif;
  }
  .canvas { position: relative; width: 1200px; height: 900px; }
  .card {
    position: absolute;
    top: 296px;
    width: 540px;
    height: 308px;
    background: var(--card);
    border-radius: 24px;
  }
  .card--front { left: 40px; }
  .card--back { left: 620px; }

  .brand { position: absolute; left: 0; right: 0; text-align: center; }
  .brand__name {
    display: inline-flex;
    align-items: center;
    gap: 10px;
    font-weight: 700;
    font-size: 38px;
    letter-spacing: 1px;
    color: var(--brand-blue);
  }
  .brand__mark { width: 16px; height: 16px; background: var(--brand-blue); }
  .brand__tagline {
    display: flex;
    align-items: center;
    justify-content: center;
    gap: 10px;
    margin-top: 4px;
    font-size: 12px;
    letter-spacing: 2.5px;
    text-transform: uppercase;
    color: var(--text-muted);
  }
  .brand__tagline::before,
  .brand__tagline::after { content: ""; width: 34px; height: 1px; background: var(--rule); }
  .card--front .brand { top: 44px; }
  .card--back .brand { top: 56px; }

  .website {
    position: absolute;
    left: 0; right: 0;
    top: 146px;
    text-align: center;
    font-size: 11px;
    color: var(--text-muted);
  }
  .services {
    position: absolute;
    left: 0; right: 0;
    top: 170px;
    text-align: center;
    font-size: 12px;
    font-weight: 700;
    color: var(--text-light);
  }
  .services span { color: var(--brand-blue); padding: 0 8px; }
  .growth-chart {
    position: absolute;
    left: 50%;
    top: 204px;
    width: 150px;
    height: 64px;
    margin-left: -75px;
  }

  .contact-list { position: absolute; left: 30px; top: 150px; list-style: none; }
  .contact-list li {
    display: flex;
    align-items: center;
    gap: 10px;
    font-size: 11px;
    color: var(--text-light);
    margin-bottom: 9px;
  }
  .contact-list svg { width: 12px; height: 12px; fill: var(--brand-blue); }

  .holder { position: absolute; right: 30px; top: 160px; text-align: right; }
  .holder__name { font-weight: 700; font-size: 20px; color: var(--brand-blue); }
  .holder__role { font-weight: 700; font-size: 11px; color: var(--text-light); margin-top: 2px; }
  .holder__address {
    font-style: normal;
    font-size: 11px;
    line-height: 1.5;
    color: var(--text-light);
    margin-top: 18px;
  }
</style>
</head>
<body>
<main class="canvas">

  <section class="card card--front">
    <div class="brand">
      <div class="brand__name"><span class="brand__mark"></span>NIVELA</div>
      <div class="brand__tagline">Auditoría &amp; Contabilidad</div>
    </div>

    <ul class="contact-list">
      <li>
        <svg viewBox="0 0 24 24"><path d="M6.6 10.8a15.1 15.1 0 0 0 6.6 6.6l2.2-2.2a1 1 0 0 1 1-.25 11.4 11.4 0 0 0 3.6.57 1 1 0 0 1 1 1V20a1 1 0 0 1-1 1A17 17 0 0 1 3 4a1 1 0 0 1 1-1h3.5a1 1 0 0 1 1 1c0 1.25.2 2.45.57 3.57a1 1 0 0 1-.25 1z"/></svg>
        +569 84125093
      </li>
      <li>
        <svg viewBox="0 0 24 24"><path d="M2 5h20v14H2zm2 2v.5l8 5 8-5V7zm0 2.9V17h16V9.9l-8 5z"/></svg>
        lorena.fuentes.araya@correoviva.cl
      </li>
      <li>
        <svg viewBox="0 0 24 24"><path d="M12 2a10 10 0 1 0 0 20 10 10 0 0 0 0-20zm0 2a8 8 0 0 1 7.7 6H4.3A8 8 0 0 1 12 4zm-7.7 8h15.4A8 8 0 0 1 12 20a8 8 0 0 1-7.7-8z"/></svg>
        www.nivelaasesorias.cl
      </li>
    </ul>

    <div class="holder">
      <div class="holder__name">Lorena Fuentes Araya</div>
      <div class="holder__role">Asesorías Laborales &amp; Contables</div>
      <address class="holder__address">
        Av. Palmeral nº 582 oficina 7<br>
        Rengo, Chile
      </address>
    </div>
  </section>

  <section class="card card--back">
    <div class="brand">
      <div class="brand__name"><span class="brand__mark"></span>NIVELA</div>
      <div class="brand__tagline">Auditoría &amp; Contabilidad</div>
    </div>
    <div class="website">www.nivelaasesorias.cl</div>
    <div class="services">Asesorías Tributarias<span>|</span>Asesorías Laborales</div>
    <svg class="growth-chart" viewBox="0 0 150 64" role="img" aria-label="Gráfico de barras de crecimiento">
      <rect x="4" y="44" width="22" height="20" fill="var(--bar-grey)"/>
      <rect x="40" y="32" width="22" height="32" fill="var(--bar-grey)"/>
      <rect x="76" y="18" width="22" height="46" fill="var(--bar-grey)"/>
      <rect x="112" y="2" width="22" height="62" fill="var(--brand-blue)"/>
    </svg>
  </section>

</main>
</body>
</html>
```